Graphic Design of Business Process

We require an eye-catching, sophisticated design of 2 business processes (attached), that will be used digitally AND for print (to be put on walls in our office).

The basic layout is attached. We require a creative, professional designer to re-design these so that they look appealing but still able to grasp all the information.

We will require vector files and editable project files for final delivery. You may refer to our website (kitefieldmedia.com.au) for an indication of our brand.

If you have any questions, please ask.

Thank you.

```html
<!DOCTYPE html>
<html lang="en">
<head>
<meta charset="utf-8">
<title>Sales to Content Funnel &amp; Content Hierarchy</title>
<link rel="stylesheet" href="https://fonts.googleapis.com/css2?family=Lato:wght@400;700;900&display=swap">
<style>
  :root {
    --ink: #4b4c4e;
    --ink-soft: #555658;
    --cyan: #19a9d9;
    --orange: #f07f22;
    --magenta: #e0479a;
    --bg-top: #c6cbce;
    --bg-bottom: #aeb3b7;
    --panel-light: #fbfbfb;
    --panel-dark: #e2e3e4;
    --divider: #ffffff;
  }
  * { margin: 0; padding: 0; box-sizing: border-box; }
  html, body { width: 800px; height: 1200px; overflow: hidden; }
  body { font-family: "Lato", Arial, sans-serif; color: var(--ink); background: var(--divider); position: relative; }

  .section { position: absolute; left: 0; width: 800px; }
  .section--funnel { top: 0; height: 580px; background: radial-gradient(ellipse at 50% 20%, #cfd4d6 0%, var(--bg-top) 45%, var(--bg-bottom) 100%); }
  .section--hierarchy { top: 615px; height: 585px; background: radial-gradient(ellipse at 50% 10%, #c9cdd0 0%, var(--bg-top) 40%, var(--bg-bottom) 100%); }

  .section-title { position: absolute; left: 0; width: 800px; text-align: center; font-weight: 900; color: var(--ink); letter-spacing: 0.5px; }
  .section--funnel .section-title { top: 72px; font-size: 40px; }
  .section--hierarchy .section-title { top: 55px; font-size: 41px; }

  .funnel-art { position: absolute; left: 0; top: 0; }

  .stage { position: absolute; text-align: center; text-transform: uppercase; }
  .stage__name { font-size: 22px; font-weight: 700; line-height: 28px; }
  .stage__task { font-size: 13px; font-weight: 700; color: var(--ink-soft); margin-top: 2px; }
  .stage__note { font-size: 8px; font-weight: 700; color: var(--ink-soft); line-height: 10px; }
  .stage__note u { text-decoration: underline; }
  .stage--awareness { left: 30px; top: 167px; width: 200px; }
  .stage--awareness .stage__name { color: var(--cyan); }
  .stage--consideration { left: 10px; top: 285px; width: 245px; }
  .stage--consideration .stage__name { color: var(--orange); }
  .stage--decision { left: 40px; top: 407px; width: 170px; }
  .stage--decision .stage__name { color: var(--magenta); }

  .flow-label { position: absolute; text-align: center; font-size: 10px; line-height: 12px; color: var(--ink-soft); text-transform: uppercase; }
  .flow-label strong { font-weight: 900; }
  .flow-label--awareness { left: 615px; top: 198px; width: 150px; }
  .flow-label--consideration { left: 555px; top: 297px; width: 120px; }
  .flow-label--convert { left: 500px; top: 423px; width: 110px; font-weight: 900; }
  .flow-label--referral { left: 560px; top: 459px; width: 70px; font-weight: 900; }

  .tier { position: absolute; left: 173px; width: 474px; height: 128px; border: 2px solid #f4f4f4; background: linear-gradient(135deg, var(--panel-light) 0%, #f0f0f0 50%, var(--panel-dark) 100%); }
  .tier--hero { top: 122px; }
  .tier--hub { top: 258px; }
  .tier--hygiene { top: 395px; }
  .tier__icon { position: absolute; left: 40px; top: 28px; width: 72px; height: 72px; }
  .tier__text { position: absolute; left: 140px; width: 282px; top: 30px; text-align: center; text-transform: uppercase; }
  .tier__name { font-size: 18px; font-weight: 900; line-height: 22px; }
  .tier__desc { font-size: 17px; font-weight: 400; color: var(--ink-soft); margin-top: 8px; letter-spacing: 0.3px; }
  .tier--hero .tier__name { color: var(--cyan); }
  .tier--hub .tier__name { color: var(--orange); }
  .tier--hygiene .tier__name { color: var(--magenta); }
  .hero-mark { position: absolute; left: 44px; top: 30px; width: 68px; height: 72px; background: var(--cyan); border-radius: 18px 34px 10px 30px; }
</style>
</head>
<body>

<section class="section section--funnel">
  <h1 class="section-title">SALES —&gt; CONTENT FUNNEL</h1>

  <svg class="funnel-art" width="800" height="580" viewBox="0 0 800 580" aria-hidden="true">
    <defs>
      <linearGradient id="layer-fill" x1="0" y1="0" x2="0" y2="1">
        <stop offset="0" stop-color="#ffffff"/>
        <stop offset="1" stop-color="#e4e5e6"/>
      </linearGradient>
      <marker id="arrowhead" markerWidth="10" markerHeight="10" refX="8" refY="5" orient="auto" markerUnits="userSpaceOnUse">
        <path d="M0,0 L10,5 L0,10 Z" fill="#4b4c4e"/>
      </marker>
    </defs>

    <!-- funnel layers -->
    <polygon points="200,142 652,142 595,258 258,258" fill="url(#layer-fill)" stroke="#f7f7f7" stroke-width="2"/>
    <polygon points="273,268 580,268 520,384 333,384" fill="url(#layer-fill)" stroke="#f7f7f7" stroke-width="2"/>
    <polygon points="346,394 503,394 425,530" fill="url(#layer-fill)" stroke="#f7f7f7" stroke-width="2"/>

    <!-- lightbulb icon -->
    <g class="icon-bulb" fill="none" stroke="#19a9d9" stroke-width="4" stroke-linecap="round">
      <path d="M414,218 a17,17 0 1 1 22,0 v8 h-22 z" fill="#19a9d9" stroke="none"/>
      <rect x="414" y="228" width="22" height="4" rx="1" fill="#19a9d9" stroke="none"/>
      <rect x="417" y="234" width="16" height="4" rx="2" fill="#19a9d9" stroke="none"/>
      <path d="M417,203 l6,6 l11,-11" stroke="#ffffff" stroke-width="3"/>
      <line x1="425" y1="170" x2="425" y2="176"/>
      <line x1="401" y1="180" x2="405" y2="184"/>
      <line x1="449" y1="180" x2="445" y2="184"/>
      <line x1="393" y1="203" x2="399" y2="203"/>
      <line x1="451" y1="203" x2="457" y2="203"/>
      <line x1="399" y1="225" x2="403" y2="222"/>
      <line x1="451" y1="225" x2="447" y2="222"/>
    </g>

    <!-- chat icon -->
    <g class="icon-chat">
      <path d="M426,308 h34 a5,5 0 0 1 5,5 v24 a5,5 0 0 1 -5,5 h-4 v10 l-10,-10 h-20 z" fill="#f07f22"/>
      <path d="M393,296 h46 a6,6 0 0 1 6,6 v28 a6,6 0 0 1 -6,6 h-30 l-12,12 v-12 h-4 a6,6 0 0 1 -6,-6 v-28 a6,6 0 0 1 6,-6 z" fill="#f07f22" stroke="#f2f2f2" stroke-width="2"/>
      <circle cx="403" cy="316" r="3.5" fill="#fff"/>
      <circle cx="416" cy="316" r="3.5" fill="#fff"/>
      <circle cx="429" cy="316" r="3.5" fill="#fff"/>
    </g>

    <!-- gears icon -->
    <g class="icon-gears" fill="#e0479a">
      <g transform="translate(418,452)">
        <circle r="15"/>
        <g>
          <rect x="-4" y="-21" width="8" height="42" rx="1"/>
          <rect x="-4" y="-21" width="8" height="42" rx="1" transform="rotate(45)"/>
          <rect x="-4" y="-21" width="8" height="42" rx="1" transform="rotate(90)"/>
          <rect x="-4" y="-21" width="8" height="42" rx="1" transform="rotate(135)"/>
        </g>
        <circle r="6" fill="#f1f1f1"/>
      </g>
      <g transform="translate(444,430)">
        <circle r="8"/>
        <rect x="-2.5" y="-12" width="5" height="24" rx="1"/>
        <rect x="-2.5" y="-12" width="5" height="24" rx="1" transform="rotate(45)"/>
        <rect x="-2.5" y="-12" width="5" height="24" rx="1" transform="rotate(90)"/>
        <rect x="-2.5" y="-12" width="5" height="24" rx="1" transform="rotate(135)"/>
        <circle r="3.5" fill="#f1f1f1"/>
      </g>
    </g>

    <!-- feedback arrows -->
    <g fill="none" stroke="#4b4c4e" stroke-width="2.5">
      <path d="M745,442 C800,400 800,250 700,250 L600,250" marker-end="url(#arrowhead)"/>
      <path d="M745,442 C765,420 765,366 700,366 L535,366" marker-end="url(#arrowhead)"/>
      <path d="M745,442 C745,462 735,469 700,469 L470,469" marker-end="url(#arrowhead)"/>
    </g>
  </svg>

  <div class="stage stage--awareness">
    <div class="stage__name">Awareness</div>
    <div class="stage__task">Identfy problem/need</div>
    <div class="stage__note">- Aspirational<br>- Market the outcome not product</div>
  </div>

  <div class="stage stage--consideration">
    <div class="stage__name">Consideration</div>
    <div class="stage__task">Evaluate alternatives</div>
    <div class="stage__note">- Why is the solution better than others<br>- How is this provider going to solve my need</div>
  </div>

  <div class="stage stage--decision">
    <div class="stage__name">Action/<br>Decision</div>
    <div class="stage__task">Present an effer</div>
    <div class="stage__note">- <u>Which</u> provider ?</div>
  </div>

  <div class="flow-label flow-label--awareness"><strong>Problem &amp; Solution</strong><br>Subject showing<br>symptoms of problem</div>
  <div class="flow-label flow-label--consideration"><strong>Providers &amp; types<br>of solution</strong><br>Subject gives name<br>to problem</div>
  <div class="flow-label flow-label--convert">Convert &amp; retain</div>
  <div class="flow-label flow-label--referral">WOM &amp;<br>Referral</div>
</section>

<section class="section section--hierarchy">
  <h2 class="section-title">CONTENT HIERARCHY</h2>

  <div class="tier tier--hero">
    <div class="hero-mark" role="img" aria-label="Flexed arm icon in cyan"></div>
    <div class="tier__text">
      <div class="tier__name">Hero</div>
      <div class="tier__desc">Tentpole campaigns</div>
    </div>
  </div>

  <div class="tier tier--hub">
    <svg class="tier__icon" viewBox="0 0 72 72" aria-hidden="true">
      <g fill="none" stroke="#f07f22" stroke-width="3">
        <line x1="40" y1="37" x2="18" y2="12"/>
        <line x1="40" y1="37" x2="60" y2="24"/>
        <line x1="40" y1="37" x2="12" y2="46"/>
        <line x1="40" y1="37" x2="56" y2="60"/>
        <circle cx="40" cy="37" r="11" fill="#f6f6f6"/>
        <circle cx="18" cy="12" r="7" fill="#f6f6f6"/>
        <circle cx="60" cy="24" r="6" fill="#f6f6f6"/>
        <circle cx="12" cy="46" r="6" fill="#f6f6f6"/>
        <circle cx="56" cy="60" r="6" fill="#f6f6f6"/>
      </g>
    </svg>
    <div class="tier__text">
      <div class="tier__name">Hub</div>
      <div class="tier__desc">Regular ``push” content</div>
    </div>
  </div>

  <div class="tier tier--hygiene">
    <svg class="tier__icon" viewBox="0 0 72 72" aria-hidden="true">
      <g fill="#e0479a">
        <path d="M10,30 a20,20 0 0 1 40,0 z"/>
        <rect x="4" y="28" width="52" height="5" rx="2"/>
        <path d="M30,12 V8 a12,12 0 0 1 24,0 V72 h-6 V8 a6,6 0 0 0 -12,0 V12 z"/>
        <path d="M12,40 q2,4 0,7 q-2,-3 0,-7z M24,40 q2,4 0,7 q-2,-3 0,-7z M36,40 q2,4 0,7 q-2,-3 0,-7z M12,54 q2,4 0,7 q-2,-3 0,-7z M24,54 q2,4 0,7 q-2,-3 0,-7z M36,54 q2,4 0,7 q-2,-3 0,-7z"/>
      </g>
    </svg>
    <div class="tier__text">
      <div class="tier__name">Hygiene</div>
      <div class="tier__desc">Always-on ``pull” content</div>
    </div>
  </div>
</section>

</body>
</html>
```